Business Card for Coach - ready to print

Design Business Card ready to order prints www.larsholm.coach

* An Overview / Background of the Business & Services
· Coaching
· Personal growth
* The Target Market / Audience you are trying to reach
· private person in different roles (self, familiy, business role)s
* Design Specifics; any preferences or ideas for Style, Colour, Imagery, etc
· See www.larsholm.coach
· "simple" design
· (small) element of surprise / unusual element

* Information that will be placed in the Business Card
· Beratung und Coaching
· Address: Lars Holm, Kesselgasse 7, CH-8517 Winterthur, Mobile +41 76 254 60 31
* Do you have an existing website or Facebook page where designers can learn more about your company?
· larsholm.coach

Target Market(s)

private person in different roles (self, familiy, business role)

Industry/Entity Type

Life Coaching

Contact Information for Business Card

Lars Holm
Kesselgasse 7
CH-8517 Winterthur

Mobile: +41 76 254 60 31
Email: laho@mailvale.ch
www.larsholm.coach

Font styles to use
Sans Serif

Colors

Designer to choose colors to be used in the design.

Requirements
Must have
• "simple" design
• element of surprise / unusual element
• Beratung & Coaching
• see www.larsholm.coach for colors and so...
Nice to have
• TA Symbol (three rings on top of each other) - unsual presentation
• QR Code of Website (see if it fits in and still looks good).

```html
<!DOCTYPE html>
<html lang="de">
<head>
<meta charset="utf-8">
<title>Lars Holm – Beratung &amp; Coaching – Visitenkarte</title>
<link href="https://fonts.googleapis.com/css2?family=Montserrat:wght@400;500;700&display=swap" rel="stylesheet">
<style>
  :root{
    --page:#3b3b3b;
    --card-dark:#4a4a4b;
    --card-light:#f4f4f4;
    --orange:#e2871b;
    --ink:#3f3f40;
    --rule:#5a5a5a;
    --white:#ffffff;
  }
  *{box-sizing:border-box;margin:0;padding:0}
  html,body{width:1200px;height:1021px;overflow:hidden}
  body{background:var(--page);font-family:"Montserrat",Arial,sans-serif;position:relative}
  .card{position:absolute;left:230px;width:740px;height:423px;border-radius:4px;box-shadow:0 8px 24px rgba(0,0,0,.35)}
  .card--front{top:60px;background:var(--card-dark)}
  .card--back{top:538px;background:var(--card-light)}

  /* front */
  .front-brand{position:absolute;inset:0;display:flex;flex-direction:column;align-items:center;justify-content:center}
  .front-brand__mark{width:46px;height:46px;background:var(--orange);margin-bottom:18px}
  .front-brand__name{color:var(--orange);font-weight:700;font-size:46px;letter-spacing:3px;line-height:1}
  .front-brand__tagline{color:var(--white);font-weight:500;font-size:25px;letter-spacing:1px;margin-top:8px}

  /* back */
  .back-brand{position:absolute;left:40px;top:0;width:250px;height:423px;display:flex;flex-direction:column;align-items:center;justify-content:center}
  .back-brand__mark{width:120px;height:120px;background:var(--orange);margin-bottom:22px}
  .back-brand__name{color:var(--ink);font-weight:700;font-size:32px;letter-spacing:2px}
  .divider{position:absolute;left:318px;top:90px;width:2px;height:243px;background:var(--rule)}
  .contact{position:absolute;left:352px;top:92px;color:var(--ink)}
  .contact__name{color:var(--orange);font-weight:700;font-size:25px;letter-spacing:1.5px;line-height:1.1}
  .contact__tagline{font-size:21px;font-weight:500;letter-spacing:.5px;margin-top:2px}
  .contact__address{font-size:21px;font-weight:500;letter-spacing:.5px;line-height:1.25;margin-top:14px}
  .contact__list{list-style:none;margin-top:12px}
  .contact__item{display:flex;align-items:center;gap:8px;font-size:21px;font-weight:500;letter-spacing:.5px;line-height:1.3}
  .contact__icon{width:18px;height:18px;flex:none}
</style>
</head>
<body>
  <section class="card card--front" aria-label="Vorderseite">
    <div class="front-brand">
      <div class="front-brand__mark"></div>
      <div class="front-brand__name">LARS HOLM</div>
      <div class="front-brand__tagline">Beratung &amp; Coaching</div>
    </div>
  </section>

  <section class="card card--back" aria-label="Rückseite">
    <div class="back-brand">
      <div class="back-brand__mark"></div>
      <div class="back-brand__name">LARS HOLM</div>
    </div>
    <div class="divider"></div>
    <div class="contact">
      <div class="contact__name">LARS HOLM</div>
      <div class="contact__tagline">Beratung &amp; Coaching</div>
      <div class="contact__address">Kesselgasse 7<br>CH-8517 Winterthur</div>
      <ul class="contact__list">
        <li class="contact__item">
          <svg class="contact__icon" viewBox="0 0 18 18"><rect x="4" y="1" width="10" height="16" rx="2" fill="none" stroke="#e2871b" stroke-width="1.6"/><circle cx="9" cy="14" r="1" fill="#e2871b"/></svg>
          +41 76 254 60 31
        </li>
        <li class="contact__item">
          <svg class="contact__icon" viewBox="0 0 18 18"><rect x="1" y="4" width="16" height="11" fill="none" stroke="#e2871b" stroke-width="1.6"/><path d="M1 4l8 6 8-6" fill="none" stroke="#e2871b" stroke-width="1.6"/></svg>
          laho@mailvale.ch
        </li>
        <li class="contact__item">
          <svg class="contact__icon" viewBox="0 0 18 18"><circle cx="9" cy="9" r="7.5" fill="none" stroke="#e2871b" stroke-width="1.5"/><ellipse cx="9" cy="9" rx="3.2" ry="7.5" fill="none" stroke="#e2871b" stroke-width="1.2"/><path d="M1.5 9h15M3 5h12M3 13h12" stroke="#e2871b" stroke-width="1.1"/></svg>
          www.larsholm.coach
        </li>
      </ul>
    </div>
  </section>
</body>
</html>
```